Zelno Vigor Iron Tempo Multi Vitamin Label Design

We need a label design for our Sports Performance Daily Multi Vitamin specially created and branded for our Zelno Vigor line for the University of Calvoria. The feel is edgy, sports nutrition. Two logos need to be incorporated... Zelno and the Collective Logo attached. The colors should be the official colors of the University of Calvoria. The font may also be the Georgia font... or the Zelno font. Or any font. A hydration product will also be created later on...so this label design may be used on many products. Please utilize the collective logo similar to the use in the attached photo. No official trademark items from the University of Calvoria should be used. Attached is also an image if the bottle (white) that will be used for the vitamin. Please use red, black, grey, white. We are looking for the front design only right now and once selected, will work on the nutrition/back label portion with the artist.

```html
<!DOCTYPE html>
<html lang="en">
<head>
<meta charset="utf-8">
<title>Zelno Vigor Sports Performance Daily Multi Vitamin Labels</title>
<link rel="stylesheet" href="https://fonts.googleapis.com/css2?family=Exo+2:ital,wght@0,600;1,900&family=Oswald:wght@500;700&display=swap">
<style>
  :root {
    --backdrop: #e6e7e8;
    --label-white: #ffffff;
    --ink-black: #0b0b0b;
    --brush-grey: #2e2f31;
    --brush-edge: #4a4b4e;
    --sport-red: #e21b24;
    --deep-red: #a3151c;
    --perf-grey: #b9bbbe;
    --silver-light: #f2f2f3;
    --silver-mid: #c3c5c8;
    --silver-dark: #8d9094;
    --badge-grey: #d9dadc;
  }
  html, body {
    margin: 0;
    padding: 0;
    width: 1200px;
    height: 1200px;
    overflow: hidden;
    background: var(--backdrop);
  }
  .canvas {
    position: relative;
    width: 1200px;
    height: 1200px;
  }
  .label {
    position: absolute;
    top: 443px;
    width: 500px;
    height: 478px;
  }
  .label--light { left: 41px; }
  .label--dark { left: 625px; }
  .brand-name {
    font-family: "Oswald", sans-serif;
    font-weight: 700;
    font-size: 52px;
    letter-spacing: 3px;
  }
  .brand-name--on-light { fill: var(--ink-black); }
  .brand-name--on-dark { fill: var(--label-white); }
  .title-sports {
    font-family: "Exo 2", sans-serif;
    font-style: italic;
    font-weight: 900;
    font-size: 78px;
    fill: var(--sport-red);
  }
  .title-performance {
    font-family: "Exo 2", sans-serif;
    font-weight: 600;
    font-size: 25px;
    letter-spacing: 7px;
    fill: var(--perf-grey);
  }
  .product-daily {
    font-family: "Oswald", sans-serif;
    font-weight: 700;
    font-size: 31px;
    fill: var(--deep-red);
  }
  .product-type {
    font-family: "Oswald", sans-serif;
    font-weight: 500;
    font-size: 17px;
    fill: var(--ink-black);
  }
  .partner-badge { fill: var(--badge-grey); stroke: var(--sport-red); stroke-width: 3; }
</style>
</head>
<body>
<main class="canvas">

  <svg class="label label--light" viewBox="0 0 500 478" xmlns="http://www.w3.org/2000/svg">
    <defs>
      <linearGradient id="silverLight" x1="0" x2="1" y1="0" y2="0">
        <stop offset="0" stop-color="#8d9094"/>
        <stop offset="0.3" stop-color="#f2f2f3"/>
        <stop offset="0.6" stop-color="#c3c5c8"/>
        <stop offset="1" stop-color="#7d8084"/>
      </linearGradient>
    </defs>
    <rect class="label-base" x="0" y="0" width="500" height="478" fill="var(--label-white)"/>
    <rect class="silver-panel" x="82" y="0" width="363" height="478" fill="url(#silverLight)"/>
    <polygon class="brush-band" role="img" aria-label="Grunge black brush stroke band" points="0,150 500,55 500,238 0,372" fill="var(--brush-grey)" opacity="0.95"/>
    <text class="brand-name brand-name--on-light" x="224" y="82" text-anchor="middle">ZELNO</text>
    <g transform="rotate(-9 258 210)">
      <text class="title-sports" x="262" y="222" text-anchor="middle">SPORTS</text>
      <text class="title-performance" x="272" y="258" text-anchor="middle">PERFORMANCE</text>
    </g>
    <text class="product-daily" x="104" y="416">DAILY</text>
    <text class="product-type" x="104" y="443">MULTI VITAMIN</text>
    <circle class="partner-badge" cx="356" cy="392" r="46"/>
  </svg>

  <svg class="label label--dark" viewBox="0 0 500 478" xmlns="http://www.w3.org/2000/svg">
    <defs>
      <linearGradient id="silverDark" x1="0" x2="1" y1="0" y2="0">
        <stop offset="0" stop-color="#8d9094"/>
        <stop offset="0.3" stop-color="#f2f2f3"/>
        <stop offset="0.6" stop-color="#c3c5c8"/>
        <stop offset="1" stop-color="#7d8084"/>
      </linearGradient>
    </defs>
    <rect class="label-base" x="0" y="0" width="500" height="478" fill="var(--label-white)"/>
    <rect class="silver-panel" x="82" y="0" width="363" height="478" fill="url(#silverDark)"/>
    <polygon class="black-top" points="0,0 500,0 500,238 0,372" fill="var(--ink-black)"/>
    <polygon class="brush-band" role="img" aria-label="Grunge dark grey brush stroke band" points="0,150 500,55 500,238 0,372" fill="var(--brush-grey)" opacity="0.85"/>
    <text class="brand-name brand-name--on-dark" x="224" y="82" text-anchor="middle">ZELNO</text>
    <g transform="rotate(-9 258 210)">
      <text class="title-sports" x="262" y="222" text-anchor="middle">SPORTS</text>
      <text class="title-performance" x="272" y="258" text-anchor="middle">PERFORMANCE</text>
    </g>
    <text class="product-daily" x="104" y="416">DAILY</text>
    <text class="product-type" x="104" y="443">MULTI VITAMIN</text>
    <circle class="partner-badge" cx="356" cy="392" r="46"/>
  </svg>

</main>
</body>
</html>
```